Venue Booking Site

I would like a venue directory and booking website designed. The idea is that end users will come to the site to find venues for weddings, parties, events etc. They will be able to find the venue based on many criteria, the most important ones are availability and location - they will be able to see in real time which venues are available for the desired dates and areas.

Venues will be able to use the website as a reservation management tool, receive payments for bookings through the site and be able to manage bookings on the go. This will be made into an app. It needs to be developed in bootstrap. Brand name to be used: Mirqona. Venue, place and space bookings.

Target audience - end users - anyone who is looking for a venue. For Community members it will provide an easy way to find a suitable venue
Outline what dates and times the venue is available
Outline costs involved in booking the venue
Search via many other criteria
It will allow the customer to book and pay for the venue online in one smooth process

Clients: Venue managers - particularly focussing on not for profit businesses eg, GHAs, community hall managers, small business managers. These people typically use paper based systems yet and do not use websites so it needs to be very user friendly. Future growth to restaurants, pubs, event venues who have a stronger familiarity with computers and who might already use their own booking management tool - so this needs to be able to link in with their system.

What need will this meet for venue managers:
This tool provides venues with greater visibility, promotion and advertising of their venue
This allows more customers to find them and book with them
This tool will be offered to not-for-profit venue managers for free to better connect them to the community
This means greater profit for these community venues
This means more revenue and jobs created in these communities

Sample of the layout / contents attached. This is not a complete site map as yet as it is a work in progress for final pages.

Small Business

5+ page

Sans Serif

eb2027

• This is a psd file only - one template for each different section, home page, search page, detailed page view, admin back end
• does not need to be coded.
• Note, the golden lantern logo jpeg files were files we were toying with using for this project- but I am happy to use the main mirqona logo- I will let you decide.

```html
<!DOCTYPE html>
<html lang="en">
<head>
<meta charset="utf-8">
<title>Mirqona – Venue, Place and Space Bookings</title>
<link rel="stylesheet" href="https://fonts.googleapis.com/css2?family=Lato:wght@400;700&family=Roboto:ital,wght@0,400;0,500;0,700;1,400&display=swap">
<style>
  :root {
    --brand-red: #d92b2b;
    --login-red: #cc3f1b;
    --brand-blue: #1a9ad6;
    --deep-blue: #176690;
    --navy: #1d4f73;
    --bar-blue: #4db3e2;
    --footer-blue: #1a8fd0;
    --ink: #2a2a2a;
    --white: #ffffff;
    --field: rgba(160, 160, 160, 0.55);
    --panel: rgba(235, 235, 235, 0.82);
  }
  * { box-sizing: border-box; margin: 0; padding: 0; }
  html, body { width: 1200px; height: 684px; overflow: hidden; }
  body { position: relative; font-family: "Roboto", Arial, sans-serif; color: var(--ink); background: var(--white); }
  .abs { position: absolute; }

  /* Header */
  .site-header { left: 0; top: 0; width: 1200px; height: 85px; background: var(--white); border-bottom: 4px solid var(--brand-blue); height: 89px; }
  .brand-mark { left: 204px; top: 28px; width: 64px; height: 36px; background: var(--brand-blue); border-radius: 4px; }
  .brand-name { left: 281px; top: 15px; font-family: "Lato", sans-serif; font-weight: 700; font-size: 34px; line-height: 40px; color: var(--brand-red); letter-spacing: 0.5px; }
  .brand-tagline { left: 282px; top: 55px; font-size: 10.5px; color: var(--ink); letter-spacing: 0.2px; }
  .header-divider { left: 471px; top: 22px; width: 1px; height: 48px; background: #cfcfcf; }
  .charity-label { left: 485px; top: 25px; font-size: 13.5px; color: var(--brand-blue); letter-spacing: 0.2px; }
  .charity-total { left: 485px; top: 43px; font-size: 21px; font-weight: 700; color: #3a3a3a; }
  .charity-total span { color: var(--brand-red); }
  .btn { display: flex; align-items: center; justify-content: center; color: var(--white); font-size: 12px; font-weight: 500; border-radius: 2px; }
  .btn-login { left: 798px; top: 32px; width: 101px; height: 31px; background: var(--login-red); }
  .btn-list { left: 909px; top: 32px; width: 102px; height: 31px; background: var(--brand-blue); }

  /* Hero */
  .hero-backdrop { left: 0; top: 89px; width: 1200px; height: 526px;
    background: radial-gradient(ellipse at 50% 20%, #d9cfc0 0%, #8a6f55 30%, #4a3424 60%, #2a1c14 100%); }

  .search-panel { left: 221px; top: 123px; width: 767px; height: 300px; background: var(--panel); border-radius: 3px; }
  .panel-title { left: 237px; top: 142px; font-size: 17px; color: var(--ink); }
  .panel-rule { left: 237px; top: 166px; width: 488px; height: 1px; background: #9a9a9a; }
  .field-label { left: 237px; font-size: 15px; color: var(--ink); }
  .field { left: 360px; width: 365px; height: 24px; background: var(--field); border-radius: 2px; font-size: 11.5px; font-style: italic; color: #555; padding: 6px 8px; line-height: 12px; }
  .field svg { position: absolute; right: 6px; top: 4px; }
  .btn-search { left: 623px; top: 375px; width: 102px; height: 23px; background: var(--brand-red); font-size: 13px; }

  .subscribe-box { left: 749px; top: 134px; width: 228px; height: 267px; background: var(--brand-blue); border: 1px solid #67bde6; border-radius: 2px; }
  .subscribe-title { left: 749px; top: 143px; width: 228px; text-align: center; color: var(--white); font-size: 17px; }
  .subscribe-rule { left: 759px; top: 167px; width: 209px; height: 1px; background: #7fcaec; }
  .subscribe-text { left: 749px; top: 180px; width: 228px; text-align: center; color: var(--white); font-size: 13.5px; }
  .subscribe-icon { left: 817px; top: 208px; }
  .sub-field { left: 759px; width: 209px; height: 24px; background: #b7e0f4; border-radius: 2px; font-size: 11px; color: #6a9bb5; padding: 6px 7px; line-height: 12px; }
  .btn-submit { left: 812px; top: 369px; width: 102px; height: 24px; background: var(--deep-blue); font-size: 13px; }

  .welcome-panel { left: 221px; top: 434px; width: 767px; height: 171px; background: rgba(40, 150, 210, 0.82); border-radius: 3px; }
  .welcome-title { left: 232px; top: 441px; font-family: "Lato", sans-serif; font-size: 19px; color: var(--white); }
  .welcome-rule { left: 232px; top: 467px; width: 738px; height: 1px; background: #8fd0ee; }
  .welcome-photo { left: 234px; top: 475px; width: 204px; height: 121px; border: 4px solid var(--white);
    background: linear-gradient(135deg, #2b1b4a 0%, #c2307a 45%, #3c7ad8 75%, #1a1030 100%); }
  .welcome-copy { left: 452px; top: 478px; width: 520px; font-family: "Lato", sans-serif; font-size: 12px; line-height: 19.6px; color: var(--white); }

  .carousel-dots { left: 1031px; top: 474px; display: flex; gap: 3px; }
  .carousel-dots span { width: 10px; height: 10px; border-radius: 50%; border: 2px solid var(--white); }
  .carousel-dots span.is-active { background: var(--white); }

  /* Recent searches */
  .recent-bar { left: 0; top: 615px; width: 1200px; height: 45px; background: var(--bar-blue); }
  .recent-title { left: 204px; top: 628px; font-family: "Lato", sans-serif; font-size: 17px; color: var(--navy); }
  .recent-item { top: 630px; font-size: 13.5px; color: var(--navy); }
  .recent-icon { top: 627px; }
  .social-dot { top: 625px; width: 27px; height: 27px; border-radius: 50%; border: 1.5px solid var(--navy); }

  .site-footer { left: 0; top: 660px; width: 1200px; height: 24px; background: var(--footer-blue); color: var(--white); font-size: 11px; text-align: center; line-height: 24px; }
  .site-footer strong { font-weight: 700; }
</style>
</head>
<body>
  <header class="abs site-header">
    <div class="abs brand-mark"></div>
    <div class="abs brand-name">MIRQONA</div>
    <div class="abs brand-tagline">VENUE, PLACE AND SPACE BOOKINGS.</div>
    <div class="abs header-divider"></div>
    <div class="abs charity-label">TOTAL RAISED FOR CHARITY:</div>
    <div class="abs charity-total"><span>$</span>40,987,480</div>
    <a class="abs btn btn-login">VENUE LOGIN</a>
    <a class="abs btn btn-list">LIST MY VENUE</a>
  </header>

  <div class="abs hero-backdrop" role="img" aria-label="Banquet hall set inside a grand wood-panelled library with chandeliers and dressed tables"></div>

  <section class="abs search-panel"></section>
  <h2 class="abs panel-title">FIND A VENUE</h2>
  <div class="abs panel-rule"></div>

  <label class="abs field-label" style="top:180px">Date of event</label>
  <div class="abs field" style="top:178px">
    <svg width="14" height="15" viewBox="0 0 14 15"><rect x="1" y="2.5" width="12" height="11" fill="none" stroke="#555" stroke-width="1.4"/><line x1="1" y1="6" x2="13" y2="6" stroke="#555" stroke-width="1.4"/><line x1="4" y1="1" x2="4" y2="4" stroke="#555" stroke-width="1.4"/><line x1="10" y1="1" x2="10" y2="4" stroke="#555" stroke-width="1.4"/></svg>
  </div>
  <label class="abs field-label" style="top:213px">Location</label>
  <div class="abs field" style="top:210px">
    <svg width="12" height="16" viewBox="0 0 12 16"><path d="M6 0C2.7 0 0 2.6 0 5.9 0 10.3 6 16 6 16s6-5.7 6-10.1C12 2.6 9.3 0 6 0z" fill="#555"/><circle cx="6" cy="6" r="2.2" fill="#bdbdbd"/></svg>
  </div>
  <label class="abs field-label" style="top:246px">Venue capacity</label>
  <div class="abs field" style="top:243px">Enter no. of people</div>
  <label class="abs field-label" style="top:279px">Venue use</label>
  <div class="abs field" style="top:276px">Search
    <svg width="14" height="10" viewBox="0 0 14 10" style="top:7px"><path d="M0 0h14L7 9z" fill="#555"/></svg>
  </div>
  <label class="abs field-label" style="top:312px">Keyword search</label>
  <div class="abs field" style="top:308px">Keyword search</div>
  <div class="abs field" style="top:341px">+ Advance Search</div>
  <a class="abs btn btn-search">SEARCH</a>

  <aside class="abs subscribe-box"></aside>
  <h2 class="abs subscribe-title">SUBSCRIBE</h2>
  <div class="abs subscribe-rule"></div>
  <p class="abs subscribe-text">Find out about deals and venues.</p>
  <svg class="abs subscribe-icon" width="92" height="76" viewBox="0 0 92 76">
    <path d="M2 30 L46 2 L90 30 L90 76 L2 76 Z" fill="var(--deep-blue)"/>
    <rect x="20" y="16" width="52" height="40" fill="var(--brand-blue)"/>
    <rect x="34" y="26" width="24" height="3" fill="var(--deep-blue)"/>
    <rect x="34" y="33" width="24" height="3" fill="var(--deep-blue)"/>
    <rect x="34" y="40" width="24" height="3" fill="var(--deep-blue)"/>
    <path d="M2 30 L46 58 L90 30 L90 76 L2 76 Z" fill="var(--deep-blue)" stroke="var(--brand-blue)" stroke-width="2"/>
    <path d="M2 76 L40 52 M90 76 L52 52" stroke="var(--brand-blue)" stroke-width="2"/>
  </svg>
  <div class="abs sub-field" style="top:300px">Name</div>
  <div class="abs sub-field" style="top:335px">E-mail</div>
  <a class="abs btn btn-submit">SUBMIT</a>

  <section class="abs welcome-panel"></section>
  <h2 class="abs welcome-title">WELCOME TO MIRQONA</h2>
  <div class="abs welcome-rule"></div>
  <div class="abs welcome-photo" role="img" aria-label="Nightclub venue with colourful stage lighting and guests at the bar"></div>
  <p class="abs welcome-copy">Lorem ipsum dolor sit amet, consectetuer adipiscing elit, sed diam nonummy nibh euismod tincidunt ut laoreet dolore magna aliquam erat volutpat. Ut wisi enim ad minim veniam, quis nostrud exerci tation ullamcorper suscipit lobortis nisl ut aliquip ex ea commodo consequat. Duis autem vel eum iriure dolor in hendrerit in vulputate velit esse molestie consequat, vel illum dolore eu feugiat nulla facilisis at vero eros et accumsan et iusto odio dignissim qui blandit praesent luptatum zzril delenit augue duis dolore te feugait nulla facilisi.</p>

  <div class="abs carousel-dots"><span></span><span class="is-active"></span><span></span><span></span></div>

  <nav class="abs recent-bar"></nav>
  <h3 class="abs recent-title">MY RECENT SEARCHES</h3>
  <svg class="abs recent-icon" style="left:398px" width="23" height="23" viewBox="0 0 23 23"><circle cx="11.5" cy="11.5" r="11.5" fill="var(--navy)"/><path d="M7 7l4.5 4.5L7 16M12 7l4.5 4.5L12 16" fill="none" stroke="var(--bar-blue)" stroke-width="2.2"/></svg>
  <span class="abs recent-item" style="left:434px">VENUE A</span>
  <svg class="abs recent-icon" style="left:501px;top:630px" width="16" height="16" viewBox="0 0 16 16"><path d="M2 2l6 6-6 6M8 2l6 6-6 6" fill="none" stroke="var(--navy)" stroke-width="2"/></svg>
  <span class="abs recent-item" style="left:532px">VENUE B</span>
  <svg class="abs recent-icon" style="left:598px;top:630px" width="16" height="16" viewBox="0 0 16 16"><path d="M2 2l6 6-6 6M8 2l6 6-6 6" fill="none" stroke="var(--navy)" stroke-width="2"/></svg>
  <span class="abs recent-item" style="left:629px">VENUE C</span>
  <span class="abs social-dot" style="left:913px"></span>
  <span class="abs social-dot" style="left:946px"></span>
  <span class="abs social-dot" style="left:980px"></span>

  <footer class="abs site-footer">© 2014. <strong>MIRQONA.</strong> All Right Reserved.</footer>
</body>
</html>
```